UPDATED BRIEF: Hypermobile EDS Book Cover Contest

I am writing a print book. I need cover designs to evaluate with your creativity. It is a nonfiction memoir meets self-help guide to living with a rare, incurable chronic illness called EDS. See attached Word doc for book details and copy. It is designed to be an inspiration story of living well with this disease so mindset is a key theme. I'm looking for all types of ideas including photography (sailboat, mountain, journey concepts), type flat designs highlighting hypermobility (a key part of the disease), including good use of color and white space. I want it to be legible, intriguing, and emotive if possible. I need someone to be able to produce and provide the production files and/or edit the final text back copy as it is not yet final. I will be sharing the contest with my fan base. I will ultimately need the cover, back cover, spine, and audio and ebook covers done all the same just reformatted to size. Print book 6x9 to be done first. I dont want to provide too much direction so you can be creative.
Updates

I uploaded a new brief for updated author name and back cover. Please update and I will start the poll. I will also extend the project timeline.

Can anyone create a design with the typeset words of hypermobile on the title being "pinched" by a string? Like holding it all together by a string?

Went on vacation/holiday

Target Market(s)

chronic illness disease victims, specifically those with Hypermobile Ehlers Danlos Syndrome (EDS), dysautonomia (POTS) or craniocervical instability in the neck

Industry/Entity Type

Self help, personal development, memoir

Font styles to use
Sans Serif

Colors
FFC000
F8CF3A
FAE287
FDF2CF
FEFAEE

Requirements
Must have
• legible, intriguing even emotive design with text or photos
Nice to have
• Potentially visually showing a journey, hypermobility, or overcoming obstacles
Should not have
• black dark backgrounds

```html
<!DOCTYPE html>
<html lang="en">
<head>
<meta charset="utf-8">
<title>Finding My Balance Every Day – Cover Spread</title>
<link rel="stylesheet" href="https://fonts.googleapis.com/css2?family=Oswald:wght@400;500;600;700&family=Open+Sans:ital,wght@0,400;0,600;0,700;1,700&family=Dancing+Script:wght@600&display=swap">
<style>
  :root {
    --ink-teal: #2f5a66;
    --accent-pink: #e2528e;
    --body-grey: #5b6166;
    --paper: #ffffff;
    --stage: #f3f3f1;
    --sky-top: #f7f5ef;
    --sky-low: #e9ece6;
    --meadow-green: #8fae7a;
    --blossom-pink: #e78db7;
    --blossom-deep: #c95b93;
    --spine-line: #d9d9d9;
  }
  * { box-sizing: border-box; margin: 0; padding: 0; }
  html, body { width: 861px; height: 1200px; overflow: hidden; }
  body {
    background: var(--stage);
    font-family: "Open Sans", Arial, sans-serif;
    position: relative;
  }

  .spread {
    position: absolute;
    top: 190px;
    left: 20px;
    width: 821px;
    height: 608px;
    display: flex;
    gap: 11px;
  }

  /* FRONT COVER */
  .front-cover {
    position: relative;
    width: 405px;
    height: 608px;
    overflow: hidden;
    box-shadow: 0 2px 8px rgba(0,0,0,.12);
  }
  .front-cover .meadow-photo {
    position: absolute; inset: 0;
    background:
      radial-gradient(ellipse 70% 30% at 50% 100%, var(--blossom-deep) 0%, transparent 70%),
      linear-gradient(180deg, var(--sky-top) 0%, var(--sky-low) 45%, var(--meadow-green) 62%, var(--blossom-pink) 78%, var(--blossom-deep) 100%);
  }
  .title-block {
    position: absolute;
    top: 34px; left: 0; right: 0;
    text-align: center;
    font-family: "Oswald", "Arial Narrow", sans-serif;
  }
  .title-lead {
    color: var(--ink-teal);
    font-weight: 500;
    font-size: 31px;
    line-height: 1.12;
    letter-spacing: .5px;
  }
  .title-lead .small { font-size: 22px; }
  .title-key {
    color: var(--accent-pink);
    font-weight: 700;
    font-size: 60px;
    line-height: 1.05;
    letter-spacing: 1px;
  }
  .subtitle {
    font-family: "Oswald", "Arial Narrow", sans-serif;
    color: var(--ink-teal);
    font-size: 11.5px;
    letter-spacing: .6px;
    margin-top: 4px;
  }
  .front-author {
    position: absolute;
    bottom: 26px; left: 0; right: 0;
    text-align: center;
    font-family: "Dancing Script", cursive;
    font-size: 30px;
    color: var(--paper);
    text-shadow: 0 1px 3px rgba(0,0,0,.25);
  }

  /* BACK COVER */
  .back-cover {
    width: 405px;
    height: 608px;
    background: var(--paper);
    padding: 30px 30px 22px;
    position: relative;
    box-shadow: 0 2px 8px rgba(0,0,0,.12);
  }
  .back-headline {
    font-family: "Oswald", "Arial Narrow", sans-serif;
    color: var(--ink-teal);
    font-weight: 600;
    font-size: 17px;
    line-height: 1.25;
    text-align: center;
    letter-spacing: .3px;
  }
  .back-copy {
    font-size: 9.5px;
    line-height: 1.5;
    color: var(--body-grey);
    margin-top: 12px;
  }
  .feature-row {
    display: flex;
    gap: 16px;
    margin: 14px 0 10px;
    align-items: flex-start;
  }
  .author-photo {
    flex: 0 0 86px;
    height: 86px;
    border-radius: 50%;
    background: radial-gradient(circle at 50% 40%, #e4d7d2 0%, #b9a8a4 70%, #8d7f7c 100%);
  }
  .feature-list { list-style: none; flex: 1; }
  .feature-list li {
    display: flex;
    gap: 8px;
    font-size: 9.5px;
    line-height: 1.35;
    color: var(--body-grey);
    margin-bottom: 7px;
  }
  .feature-list svg { flex: 0 0 12px; margin-top: 1px; }
  .pull-quote {
    font-style: italic;
    font-weight: 700;
    color: var(--accent-pink);
    font-size: 17px;
    text-align: center;
    margin: 14px 0 6px;
  }
  .back-url {
    position: absolute;
    right: 30px; bottom: 22px;
    font-family: "Oswald", "Arial Narrow", sans-serif;
    color: var(--ink-teal);
    font-size: 10px;
    letter-spacing: .6px;
  }

  /* SPINE */
  .spine {
    position: absolute;
    top: 840px;
    left: 20px;
    width: 821px;
    height: 46px;
    background: var(--paper);
    border: 1px solid var(--spine-line);
    display: flex;
    align-items: center;
    justify-content: space-between;
    padding: 0 26px;
    font-family: "Oswald", "Arial Narrow", sans-serif;
    color: var(--ink-teal);
    font-weight: 600;
    font-size: 17px;
    letter-spacing: .6px;
  }
  .spine .spine-key { color: var(--accent-pink); }
</style>
</head>
<body>

<main class="spread">
  <section class="front-cover">
    <div class="meadow-photo" role="img" aria-label="Photograph of a woman standing in a field of pink flowers under a pale sky"></div>
    <div class="title-block">
      <div class="title-lead">FINDING MY BALANCE EVERY DAY<br><span class="small">WHEN</span> I'M STILL</div>
      <div class="title-key">UNSTOPPABLE</div>
      <div class="subtitle">BUILD A BRIGHTER DAILY LIFE WITH LOOSE JOINTS AND LOW ENERGY</div>
    </div>
    <div class="front-author">Marnie Hale</div>
  </section>

  <section class="back-cover">
    <h2 class="back-headline">THE GENTLE GUIDE TO LIVING WELL WITH A RARE LIFELONG CONDITION</h2>
    <p class="back-copy">This book blends personal story with practical tools. It shows how a person can live fully with a rare condition, build steady habits, and protect body and mind. You will find honest lessons, simple routines, and hope for each hard day ahead.</p>
    <p class="back-copy">Finding My Balance Every Day gives readers a clear path through doctors, diets, and daily limits, so they can move forward with confidence.</p>

    <div class="feature-row">
      <div class="author-photo" role="img" aria-label="Portrait photograph of the author"></div>
      <ul class="feature-list">
        <li><svg width="12" height="12" viewBox="0 0 12 12"><path d="M1.5 6.5 L4.5 9.5 L10.5 2.5" fill="none" stroke="#e2528e" stroke-width="2"/></svg>Personal tales that show what helped and what did not</li>
        <li><svg width="12" height="12" viewBox="0 0 12 12"><path d="M1.5 6.5 L4.5 9.5 L10.5 2.5" fill="none" stroke="#e2528e" stroke-width="2"/></svg>Gentle exercises and routines to support joints</li>
        <li><svg width="12" height="12" viewBox="0 0 12 12"><path d="M1.5 6.5 L4.5 9.5 L10.5 2.5" fill="none" stroke="#e2528e" stroke-width="2"/></svg>Guidance for talking with your care team</li>
        <li><svg width="12" height="12" viewBox="0 0 12 12"><path d="M1.5 6.5 L4.5 9.5 L10.5 2.5" fill="none" stroke="#e2528e" stroke-width="2"/></svg>Ways to keep mindset strong on tough days</li>
      </ul>
    </div>

    <p class="pull-quote">"A true companion for every hard day"</p>
    <p class="back-copy">This book was written to lift up anyone facing a long illness. It speaks to patients, families, and friends who want to understand and to help.</p>
    <p class="back-copy">Marnie draws on years of her own care to offer warmth and clear steps. Her voice is kind, direct, and full of hope.</p>

    <div class="back-url">WWW.MARNIEHALEJOURNEY.COM</div>
  </section>
</main>

<aside class="spine">
  <span>FINDING MY BALANCE EVERY DAY WHEN I'M STILL <span class="spine-key">UNSTOPPABLE</span></span>
  <span>MARNIE HALE</span>
</aside>

</body>
</html>
```